Maison Lumet is a premium domestic placement company and a concept of modern etiquette and a manueri

Maison Lumet is a premium domestic placements agency delivering the most professional caliber of domestic professionals to suit even the most demanding, challenging and refined household tasks.

Based in Dubai, Maisone Lumet the world of Maison Lumet is representing the finest.

We genuinely strive to find the best, recruit the right ones and invest our time and resources for that perfect match.

~ Career Nannies ~
~ Etiquette Governesses ~
~ Royal Protocol Attendees ~
~ Formal Palace Personnel ~
~ Official Butler ~
~ World Class Chefs ~
~ Skilled Housekeepers ~
~ Experienced Babynurses ~
~ Domestic Couples ~
~ Professional Laundresses ~
~ Personal Beautician ~
~ Enthusiastic Chauffeurs ~
~ Gourmet Cooks ~

WEB SITE BRIEF:

Style: clean, classy, refined and screaming luxury - you may see sample i like: www.corvellahouseline.com

Colors: I like black and white with a touch of pink (burned sugar more specifically)

Communicate: The images and the web should communicate class and royalty as i will be working with lots of royal families in the Region.

Images selection: this is very important to me has to be with white, black, and perhaps a touch of pink - just to get along with my logo second line.
1. one image may be a palace
2. may be a housekeeper or a butler
3. something etiquette related! or your
PS. Do not limit to those, its just mine idea and also i don't know why but i prefer images without faces - otherwise looks like endorsement and strong personalization to a face that i dont even know

Note: The pictures i have attached are tentative only

Explanation of my web structure: 1 excel page are the web links 2 are the side links, i want them to be like a sliding tips, that you click to see the next 3 social media i will start with

Standards: You may use my logo (middle icon) as a graphic idea and/or whatever you decide i like consistency - in the colors you use, style and all.

General: Easy to navigate

Thank you all in advance & Enjoy the journey

Marguerite

Target Market(s)

- Royal families and VIP's in Middle East
- Families and families with kids
- Mid and High-end segment singles
- Hotels HR departments
- Companies HR departments
- Celebrities ;)

Industry/Entity Type

It Company

Requirements
Must have
• Standards again of design, i don't like mixed style of photography and drawing and sketches all in one. Think there should be an idea in the backbone
Nice to have
• Clean, i like simple things in life
• Elegant and luxury, reliability and care - that should be the message
• on the MAIN side might have one banner that shows my value added package VIP Maison Lumet consisted of the following:
• - priority served contract
• - draw from the best candidates
• - dedicated consultant
• - FREE couture uniform
• - meeting at your choice
• - FREE training from the Maison Lumet advanced manual
• - FREE cooking book
• - Follow up visit/call
Should not have
• 1. variety of styles as said
• 2. images that are used from others in the same industry and styles
• 3. very big letters - prefer smaller fonts
• 4. illustrations that look cheap

```html
<!DOCTYPE html>
<html lang="en">
<head>
<meta charset="utf-8">
<title>Maison Lumet Nanny Manuel</title>
<link rel="stylesheet" href="https://fonts.googleapis.com/css2?family=Lora:ital,wght@0,400;1,400&family=Open+Sans:wght@400&display=swap">
<style>
  :root {
    --ink: #3a3a3a;
    --bar: #474747;
    --muted: #777777;
    --heading: #b9b9b9;
    --pink: #e8739a;
    --soft-pink: #f59cae;
    --panel: #f2f2f2;
    --chip: #ececec;
    --ruby: #c0332c;
    --white: #ffffff;
  }
  * { box-sizing: border-box; margin: 0; padding: 0; }
  html, body { width: 1200px; height: 900px; overflow: hidden; background: var(--white); }
  body { position: relative; font-family: "Lora", Georgia, serif; color: var(--ink); }

  .top-bar { position: absolute; left: 91px; top: 0; width: 1019px; height: 16px; background: var(--bar); }

  .brand { position: absolute; left: 91px; top: 138px; width: 272px; text-align: center; }
  .brand-name { font-family: "Lora", Georgia, serif; font-size: 27px; letter-spacing: 1px; color: #1d1d1d; text-transform: uppercase; }
  .brand-tagline { margin-top: 44px; font-size: 11.5px; letter-spacing: 0.6px; color: var(--pink); text-transform: uppercase; }

  .main-nav { position: absolute; right: 90px; top: 150px; display: flex; gap: 14px; }
  .main-nav a { font-family: "Open Sans", Arial, sans-serif; font-size: 13px; color: var(--muted); text-decoration: none; text-transform: uppercase; padding: 2px 7px; line-height: 18px; height: 22px; }
  .main-nav a.is-active { background: var(--chip); }

  .feature-photo { position: absolute; left: 89px; top: 309px; width: 272px; height: 309px;
    background: linear-gradient(100deg, #b08a4a 0%, #d9c08a 22%, #e9ebe8 45%, #c9ced2 62%, #f3f3f1 80%, #a27c45 100%); }

  .content { position: absolute; left: 399px; top: 304px; width: 470px; }
  .content h1 { font-weight: 400; font-size: 20.5px; color: var(--heading); text-transform: uppercase; letter-spacing: 0.2px; }
  .content p { font-size: 13.6px; line-height: 20px; margin-top: 22px; }
  .content p:first-of-type { margin-top: 30px; }
  .content .brand-link { color: var(--pink); text-transform: uppercase; }
  .download-button { position: absolute; left: -6px; top: 217px; width: 304px; height: 22px; background: var(--chip);
    font-family: "Open Sans", Arial, sans-serif; font-size: 12px; color: var(--muted); line-height: 22px; padding-left: 6px; text-transform: uppercase; text-decoration: none; }

  .side-nav { position: absolute; left: 904px; top: 308px; width: 206px; height: 140px; background: var(--panel); padding: 11px 0 0 14px; }
  .side-nav a { display: block; font-family: "Open Sans", Arial, sans-serif; font-size: 12px; line-height: 20px; color: var(--muted); text-decoration: none; text-transform: uppercase; }
  .side-nav a.is-active { color: var(--pink); }

  .tips { position: absolute; left: 904px; top: 455px; width: 206px; }
  .tip { height: 74px; margin-bottom: 2px; background: var(--ruby); color: var(--white); text-align: center; padding-top: 10px; }
  .tip-title { font-style: italic; font-size: 14.5px; line-height: 18px; }
  .tip-more { display: block; margin-top: 2px; font-family: "Open Sans", Arial, sans-serif; font-size: 10.5px; color: var(--soft-pink); text-transform: uppercase; }

  .follow { position: absolute; left: 904px; top: 772px; display: flex; align-items: center; }
  .follow-label { font-family: "Open Sans", Arial, sans-serif; font-size: 13px; color: #555; text-transform: uppercase; margin-right: 20px; }
  .social-square { width: 20px; height: 20px; border: 1px solid #cfcfcf; background: #f7f7f7; margin-right: 4px; }

  .footer-links { position: absolute; left: 91px; top: 884px; display: flex; gap: 16px; }
  .footer-links a { font-family: "Open Sans", Arial, sans-serif; font-size: 10.5px; color: var(--muted); text-decoration: none; text-transform: uppercase; }
  .footer-bar { position: absolute; left: 238px; top: 887px; width: 870px; height: 13px; background: var(--bar); }
</style>
</head>
<body>
  <div class="top-bar"></div>

  <header class="brand">
    <div class="brand-name">Maison Lumet</div>
    <div class="brand-tagline">Premium Domestic</div>
  </header>

  <nav class="main-nav">
    <a href="#">About</a>
    <a href="#">Clients</a>
    <a href="#" class="is-active">Candidates</a>
    <a href="#">Services</a>
    <a href="#">VIP &amp; Royal</a>
    <a href="#">Media</a>
    <a href="#">Contact Us</a>
  </nav>

  <div class="feature-photo" role="img" aria-label="Housekeeper in grey uniform and white apron arranging a silver tea service beside a window with gold curtains"></div>

  <main class="content">
    <h1>Maison Lumet Nanny Manuel</h1>
    <p>Those are Maison Lumet Nannies considerations and points to be taken and studied prior to attending interview and during your tenancy with the family.</p>
    <p>Once a nanny passes through the process of registration with <span class="brand-link">Maison Lumet</span>, you are required to study those and make sure are applied in your new post, utmost professionalism and care in your new home with one of our respected clients.</p>
    <a href="#" class="download-button">Click to download the guide book for nanny</a>
  </main>

  <aside class="side-nav">
    <a href="#">Candidate Requirements</a>
    <a href="#">International Placements</a>
    <a href="#">Candidate Registration Form</a>
    <a href="#" class="is-active">Maison Lumet Nanny Manuel</a>
    <a href="#">Testimonials</a>
  </aside>

  <section class="tips">
    <div class="tip"><div class="tip-title">Everyday<br>Etiquettes &amp; Courtesies</div><span class="tip-more">Learn more</span></div>
    <div class="tip"><div class="tip-title">Table Setting<br>Etiquettes</div><span class="tip-more">Learn more</span></div>
    <div class="tip"><div class="tip-title">Etiquettes<br>for Kids</div><span class="tip-more">Learn more</span></div>
    <div class="tip"><div class="tip-title">Spirituality<br>for Kids</div><span class="tip-more">Learn more</span></div>
  </section>

  <div class="follow">
    <span class="follow-label">Follow us</span>
    <span class="social-square"></span>
    <span class="social-square"></span>
    <span class="social-square"></span>
    <span class="social-square"></span>
    <span class="social-square"></span>
  </div>

  <footer>
    <div class="footer-links"><a href="#">Privacy Policy</a><a href="#">Legal</a></div>
    <div class="footer-bar"></div>
  </footer>
</body>
</html>
```